JT & WE Shearing Pty Ltd

We already have an existing logo created by Lumen Quarry however we have restructured to a company. We would like someone to add Pty Ltd to our business name please.

Colors

Designer to choose only greyscale colors for use in the design.

```html
<!DOCTYPE html>
<html lang="en">
<head>
<meta charset="utf-8">
<title>JT &amp; WE Shearing Pty Ltd — Business Card</title>
<link href="https://fonts.googleapis.com/css2?family=Noto+Serif:wght@400;700&display=swap" rel="stylesheet">
<style>
  :root {
    --page: #d9d9d9;
    --card: #1b1b1c;
    --card-edge: #262627;
    --gloss: #3b3b3d;
    --ink: #f2f2f2;
    --ink-soft: #c9c9c9;
    --rule: #8a8a8a;
  }
  * { box-sizing: border-box; margin: 0; padding: 0; }
  html, body { width: 1200px; height: 800px; overflow: hidden; }
  body {
    background: var(--page);
    font-family: "Noto Serif", Georgia, serif;
    display: flex;
    flex-direction: column;
    align-items: center;
    justify-content: center;
    gap: 48px;
  }
  .card {
    width: 600px;
    height: 340px;
    background: var(--card);
    border: 1px solid var(--card-edge);
    border-radius: 22px;
    position: relative;
    overflow: hidden;
  }
  .card--front {
    display: flex;
    align-items: center;
    justify-content: center;
  }
  .brand {
    display: flex;
    align-items: center;
    gap: 14px;
  }
  .brand__dot {
    width: 26px;
    height: 26px;
    border-radius: 50%;
  }
  .brand__name {
    font-weight: 700;
    letter-spacing: 0.01em;
    white-space: nowrap;
  }
  .card--front .brand__name { color: var(--gloss); font-size: 36px; }
  .card--front .brand__dot { background: var(--gloss); }

  .card--back {
    display: grid;
    grid-template-columns: 1fr 1px 1fr;
    align-items: center;
    padding: 0 40px;
    column-gap: 30px;
  }
  .card--back .brand { justify-content: center; }
  .card--back .brand__name { color: var(--ink); font-size: 19px; }
  .card--back .brand__dot { background: var(--ink); width: 18px; height: 18px; }
  .divider {
    width: 1px;
    height: 150px;
    background: var(--rule);
  }
  .contact { color: var(--ink); }
  .contact__name {
    font-weight: 700;
    font-size: 17px;
    letter-spacing: 0.06em;
    text-transform: uppercase;
  }
  .contact__role {
    font-size: 13px;
    color: var(--ink-soft);
    margin: 2px 0 16px;
  }
  .contact__line {
    display: flex;
    align-items: center;
    gap: 9px;
    font-size: 12.5px;
    color: var(--ink-soft);
    margin-bottom: 6px;
  }
  .contact__icon {
    width: 18px;
    height: 18px;
    flex: none;
  }
  .contact__company {
    font-weight: 700;
    font-size: 13px;
    margin-top: 14px;
  }
  .contact__address {
    font-size: 12.5px;
    color: var(--ink-soft);
    margin-top: 3px;
  }
</style>
</head>
<body>
  <section class="card card--front" aria-label="Card front">
    <div class="brand">
      <span class="brand__dot"></span>
      <span class="brand__name">JT &amp; WE Shearing Pty Ltd</span>
    </div>
  </section>

  <section class="card card--back" aria-label="Card back">
    <div class="brand">
      <span class="brand__dot"></span>
      <span class="brand__name">JT &amp; WE Shearing Pty Ltd</span>
    </div>
    <div class="divider"></div>
    <div class="contact">
      <p class="contact__name">Liam Carter</p>
      <p class="contact__role">President</p>
      <p class="contact__line">
        <svg class="contact__icon" viewBox="0 0 18 18" aria-hidden="true">
          <circle cx="9" cy="9" r="9" fill="#f2f2f2"/>
          <rect x="6" y="4" width="6" height="10" rx="1.2" fill="none" stroke="#1b1b1c" stroke-width="1.3"/>
          <line x1="8" y1="12" x2="10" y2="12" stroke="#1b1b1c" stroke-width="1.1"/>
        </svg>
        Mob 0491570156
      </p>
      <p class="contact__line">
        <svg class="contact__icon" viewBox="0 0 18 18" aria-hidden="true">
          <circle cx="9" cy="9" r="9" fill="#f2f2f2"/>
          <rect x="4.5" y="5.5" width="9" height="7" rx="0.8" fill="none" stroke="#1b1b1c" stroke-width="1.2"/>
          <polyline points="4.8,6 9,9.5 13.2,6" fill="none" stroke="#1b1b1c" stroke-width="1.2"/>
        </svg>
        jtweshearing@mailbox.net
      </p>
      <p class="contact__company">JT &amp; WE Shearing Pty Ltd</p>
      <p class="contact__address">PO Box 418 Eastfield WA 6512</p>
    </div>
  </section>
</body>
</html>
```